Stationery Design Project

Need stationery based on logo

Stationery should include:

Letterhead-should include logo at the top, and contact info at the bottom
Envelope should include mailing address  at top left corner (Varrick Study Partners, 4807 Harlow...)
PPT slide should include Logo only
Cover page should just include logo

Requirements
Must have
• Based on logo

```html
<!DOCTYPE html>
<html lang="en">
<head>
<meta charset="utf-8">
<title>Varrick Study Partners – Stationery</title>
<link rel="stylesheet" href="https://fonts.googleapis.com/css2?family=Questrial&family=Montserrat:wght@700&display=swap">
<style>
:root{
  --brand:#9ab84a;
  --brand-dark:#86a33b;
  --paper:#ffffff;
  --backdrop:#ececea;
  --shadow:rgba(0,0,0,.18);
}
*{box-sizing:border-box;margin:0;padding:0}
html,body{width:1200px;height:1149px;overflow:hidden}
body{background:var(--backdrop);position:relative;font-family:"Questrial",sans-serif;color:var(--brand)}
.sheet{position:absolute;background:var(--paper);box-shadow:2px 3px 8px var(--shadow)}
.rule{position:absolute;background:var(--brand)}
.wordmark{font-family:"Questrial",sans-serif;text-transform:uppercase;letter-spacing:2px;line-height:1.05;text-align:center;color:var(--brand);display:flex;flex-direction:column;align-items:center;gap:3px}
.wordmark .mark-square{width:12px;height:12px;background:currentColor;margin-bottom:3px}
.on-green{color:var(--paper)}
.contact{position:absolute;font-size:14px;line-height:17px;color:var(--brand)}

/* letterhead */
.letterhead{left:334px;top:0;width:810px;height:1149px}
.letterhead .wordmark{position:absolute;left:392px;top:34px;font-size:17px;width:90px}
.letterhead .wordmark{left:58px}
.letterhead .site{position:absolute;right:34px;bottom:38px;font-size:14px;font-style:italic}

/* business card, portrait */
.card-front{left:71px;top:75px;width:184px;height:335px;background:var(--brand);box-shadow:2px 3px 8px var(--shadow)}
.card-front .rule{background:var(--paper)}
.card-front .wordmark{position:absolute;left:0;right:0;top:48px;font-size:15px}
.card-front .holder{position:absolute;left:0;right:0;top:145px;text-align:center;color:var(--paper);font-size:12.5px;line-height:14px}
.card-front .holder-name{font-family:"Montserrat",sans-serif;font-weight:700;font-size:15px;letter-spacing:.5px;margin-bottom:2px}
.card-front .contact{left:0;right:0;top:272px;text-align:center;color:var(--paper);font-size:11px;line-height:14px}

/* business card, landscape */
.card-back{left:317px;top:218px;width:342px;height:196px}
.card-back .wordmark{position:absolute;left:28px;top:64px;width:98px;font-size:15px}
.card-back .site{position:absolute;left:140px;top:93px;font-size:11.5px;font-style:italic}

/* envelope */
.envelope{left:68px;top:430px;width:935px;height:405px}
.envelope .wordmark{position:absolute;left:34px;top:28px;width:100px;font-size:16px}
.envelope .contact{left:161px;top:32px;font-size:14px;line-height:16.5px}
.envelope .contact em{font-style:italic}

/* disc */
.disc{position:absolute;left:603px;top:642px;width:464px;height:464px}
.disc .wordmark{position:absolute;left:0;right:0;top:88px;font-size:27px;letter-spacing:4px}
.disc-label{position:absolute;left:96px;top:293px;width:284px;height:96px}
</style>
</head>
<body>

<section class="sheet letterhead" aria-label="Letterhead">
  <div class="rule" style="left:28px;top:24px;width:3px;height:72px"></div>
  <div class="rule" style="left:28px;top:24px;width:105px;height:3px"></div>
  <div class="rule" style="left:582px;top:22px;width:208px;height:3px"></div>
  <div class="rule" style="left:787px;top:22px;width:3px;height:60px"></div>
  <div class="rule" style="left:787px;top:915px;width:3px;height:195px"></div>
  <div class="wordmark"><span class="mark-square"></span><span>Varrick</span><span>Study</span></div>
  <address class="contact" style="left:37px;top:1052px;font-style:normal">
    4807 Harlow Drive<br>Fairview, OR 97024<br>Phone: 503-555-0148<br><em>email: em@varrickstudy.com</em>
  </address>
  <div class="site">http://www.varrickstudy.com</div>
</section>

<section class="card-front" aria-label="Business card front">
  <div class="rule" style="left:11px;top:10px;width:2px;height:130px"></div>
  <div class="rule" style="left:11px;top:10px;width:75px;height:2px"></div>
  <div class="rule" style="left:171px;top:205px;width:2px;height:123px"></div>
  <div class="wordmark on-green"><span class="mark-square"></span><span>Varrick</span><span>Study</span></div>
  <div class="holder">
    <div class="holder-name">ELENA MARSH</div>
    <div>Principal</div>
    <div>Varrick Study Partners, LLC</div>
  </div>
  <address class="contact" style="font-style:normal">
    4807 Harlow Drive<br>Fairview, OR 97024<br>Phone: 503-555-0148<br>em@varrickstudy.com
  </address>
</section>

<section class="sheet card-back" aria-label="Business card back">
  <div class="rule" style="left:273px;top:16px;width:61px;height:2px"></div>
  <div class="rule" style="left:332px;top:16px;width:2px;height:60px"></div>
  <div class="rule" style="left:132px;top:60px;width:2px;height:72px"></div>
  <div class="rule" style="left:273px;top:186px;width:61px;height:2px"></div>
  <div class="rule" style="left:332px;top:125px;width:2px;height:63px"></div>
  <div class="wordmark"><span class="mark-square"></span><span>Varrick</span><span>Study</span></div>
  <div class="site">http://varrickstudy.com</div>
</section>

<section class="sheet envelope" aria-label="Envelope">
  <div class="rule" style="left:16px;top:16px;width:280px;height:3px"></div>
  <div class="rule" style="left:16px;top:16px;width:3px;height:374px"></div>
  <div class="rule" style="left:912px;top:16px;width:3px;height:366px"></div>
  <div class="rule" style="left:147px;top:22px;width:2px;height:80px"></div>
  <div class="wordmark"><span class="mark-square"></span><span>Varrick</span><span>Study</span></div>
  <address class="contact" style="font-style:normal">
    4807 Harlow Drive<br>Fairview, OR 97024<br>Phone: 503-555-0148<br><em>http://www.varrickstudy.com</em>
  </address>
</section>

<section class="disc" aria-label="Disc label">
  <svg width="464" height="464" viewBox="0 0 464 464" style="position:absolute;left:0;top:0">
    <circle cx="232" cy="232" r="232" fill="var(--brand)"/>
    <circle cx="232" cy="232" r="66" fill="var(--brand-dark)" stroke="#a9c65c" stroke-width="2"/>
    <circle cx="232" cy="232" r="34" fill="var(--backdrop)"/>
  </svg>
  <div class="wordmark on-green"><span class="mark-square" style="width:16px;height:16px"></span><span>Varrick</span><span>Study</span></div>
  <svg class="disc-label" viewBox="0 0 284 96" aria-hidden="true">
    <g stroke="#ffffff" fill="none">
      <path d="M0 2H284V30" stroke-width="3"/>
      <path d="M0 40V94H135" stroke-width="3"/>
      <g stroke-width="1" stroke-dasharray="3 2" opacity=".9">
        <line x1="12" y1="15" x2="272" y2="15"/>
        <line x1="12" y1="34" x2="272" y2="34"/>
        <line x1="12" y1="52" x2="272" y2="52"/>
        <line x1="12" y1="70" x2="272" y2="70"/>
        <line x1="12" y1="85" x2="272" y2="85"/>
      </g>
    </g>
  </svg>
</section>

</body>
</html>
```